we need an experienced designer to design the tube for our toothpaste

Design guidelines:
1. On the front side, our product logo (‘Q2786’) should be prominent enough.
2. Our brand logo (‘quorlume’) could be small-size and it's just a trademark indeed.

Some information here for your reference:
1. The color of toothpaste cap is white.
2. We hope that the primary color in the design is blue.
3.‘F’ in ‘Q2786’ stands for ‘quorlume’ and ‘fluoride’.
4. We will use aluminum-plastic composite materials to make toothpaste tubes. In addition to the design, we also hope that you can make relevant suggestions on the special requirements of printing.

At last, we hope that you could submit both 2D design and 3D visual effects.

Attachments:

Colors
0094D4
00A9DD
6FCCEA
C7EBF8
E9F6FB

Requirements
Must have
• as attached

```html
<!DOCTYPE html>
<html lang="en">
<head>
<meta charset="utf-8">
<title>Q2786 Orthodontic Toothpaste – Tube Label</title>
<link rel="stylesheet" href="https://fonts.googleapis.com/css2?family=Poppins:wght@700;800&family=Arimo:ital,wght@0,700;1,700&family=Barlow+Condensed:wght@400;500&display=swap">
<style>
  :root {
    --blue: #0094D4;
    --blue-deep: #0077C4;
    --cyan: #00A9DD;
    --sky: #6FCCEA;
    --mist: #C7EBF8;
    --pale: #E9F6FB;
    --ink: #111418;
    --body-ink: #2a2f33;
    --backdrop: #ADA5A3;
    --white: #ffffff;
  }
  * { margin: 0; padding: 0; box-sizing: border-box; }
  html, body { width: 1200px; height: 1062px; overflow: hidden; }
  body { background: var(--backdrop); position: relative; font-family: "Arimo", Arial, sans-serif; }

  .label { position: absolute; left: 100px; width: 1000px; height: 390px; overflow: hidden; }
  .label--front { top: 110px; }
  .label--back { top: 560px; }
  .label__bg { position: absolute; inset: 0; width: 100%; height: 100%; }

  .kicker { position: absolute; left: 150px; top: 78px; font: italic 700 26px/1 "Arimo", Arial, sans-serif; color: var(--blue); letter-spacing: 0.3px; }
  .product-name { position: absolute; left: 146px; top: 112px; font: 800 156px/1 "Poppins", sans-serif; color: var(--blue); letter-spacing: -4px; }
  .product-dot { position: absolute; left: 682px; top: 92px; width: 42px; height: 42px; border-radius: 50%; background: var(--blue); }
  .strength { position: absolute; left: 152px; top: 272px; width: 273px; height: 38px; background: var(--blue); color: var(--white); font: 700 20px/38px "Poppins", sans-serif; text-align: center; letter-spacing: 0.5px; }
  .claims { position: absolute; left: 444px; top: 272px; font: 700 14.5px/1.33 "Arimo", Arial, sans-serif; color: var(--ink); }
  .variant { position: absolute; left: 760px; top: 322px; font: 700 19px/1.3 "Arimo", Arial, sans-serif; color: var(--ink); }

  .brand { position: absolute; display: flex; align-items: center; gap: 6px; font: 700 28px/1 "Poppins", sans-serif; color: var(--white); }
  .brand__dot { width: 9px; height: 9px; border-radius: 50%; background: var(--white); }
  .brand--front { left: 806px; top: 88px; }
  .brand--back { left: 808px; top: 292px; font-size: 26px; }

  .care-column { position: absolute; left: 115px; top: 0; width: 175px; height: 100%; background: var(--blue); color: var(--white); }
  .care-title { position: absolute; left: 20px; top: 54px; font: 700 17px/22px "Arimo", Arial, sans-serif; }
  .care-art { position: absolute; left: 18px; top: 150px; width: 116px; height: 130px; border-radius: 10px; background: linear-gradient(180deg, #f3f6f7 0%, #ec7a86 55%, #e2606c 100%); }
  .care-list { position: absolute; left: 12px; top: 284px; list-style: none; font: 700 15px/19px "Arimo", Arial, sans-serif; }
  .care-list li::before { content: "•"; margin-right: 3px; }

  .usage { position: absolute; left: 324px; top: 72px; width: 400px; font: 400 19px/25px "Barlow Condensed", sans-serif; color: var(--body-ink); }
  .usage p + p { margin-top: 10px; }
  .usage__head { color: var(--blue); font-weight: 500; }

  .warnings { position: absolute; right: 78px; top: 48px; text-align: right; font: 400 22px/31px "Barlow Condensed", sans-serif; color: var(--white); }
  .warnings__head { font-weight: 500; }
</style>
</head>
<body>

<section class="label label--front" aria-label="Front of tube">
  <svg class="label__bg" viewBox="0 0 1000 390" preserveAspectRatio="none" aria-hidden="true">
    <defs>
      <linearGradient id="frontBody" x1="0" y1="0" x2="0" y2="1">
        <stop offset="0" stop-color="#C3D2D8"/>
        <stop offset="0.35" stop-color="#F4F8FA"/>
        <stop offset="0.7" stop-color="#E6EEF1"/>
        <stop offset="1" stop-color="#B9CBD3"/>
      </linearGradient>
      <linearGradient id="frontSweep" x1="0" y1="0" x2="1" y2="1">
        <stop offset="0" stop-color="#0077C4"/>
        <stop offset="0.35" stop-color="#00A9DD"/>
        <stop offset="0.6" stop-color="#6FCCEA"/>
        <stop offset="1" stop-color="#0077C4"/>
      </linearGradient>
    </defs>
    <rect width="1000" height="390" fill="url(#frontBody)"/>
    <rect x="0" width="112" height="390" fill="#D6E1E5"/>
    <path d="M740 0 C 810 60, 800 230, 540 390 L1000 390 L1000 0 Z" fill="url(#frontSweep)"/>
    <rect x="956" width="44" height="390" fill="#0A7FCB"/>
    <g stroke="#0069B3" stroke-width="2">
      <line x1="956" y1="20" x2="1000" y2="20"/><line x1="956" y1="50" x2="1000" y2="50"/>
      <line x1="956" y1="80" x2="1000" y2="80"/><line x1="956" y1="110" x2="1000" y2="110"/>
      <line x1="956" y1="140" x2="1000" y2="140"/><line x1="956" y1="170" x2="1000" y2="170"/>
      <line x1="956" y1="200" x2="1000" y2="200"/><line x1="956" y1="230" x2="1000" y2="230"/>
      <line x1="956" y1="260" x2="1000" y2="260"/><line x1="956" y1="290" x2="1000" y2="290"/>
      <line x1="956" y1="320" x2="1000" y2="320"/><line x1="956" y1="350" x2="1000" y2="350"/>
    </g>
  </svg>
  <div class="kicker">ORTHODONTIC TOOTHPASTE</div>
  <div class="product-name">Q2786</div>
  <div class="product-dot"></div>
  <div class="strength">FLUORIDE 1450 PPM</div>
  <div class="claims">ENHANCED CAVITY PREVENTION AND GUM PROTECTION<br>FOR USE WHEN WEARING METAL BRACES AND CLEAR ALIGNERS</div>
  <div class="variant">Cool Mint<br>NET WT. 85g</div>
  <div class="brand brand--front">quorlume<span class="brand__dot"></span></div>
</section>

<section class="label label--back" aria-label="Back of tube">
  <svg class="label__bg" viewBox="0 0 1000 390" preserveAspectRatio="none" aria-hidden="true">
    <defs>
      <linearGradient id="backBody" x1="0" y1="0" x2="0" y2="1">
        <stop offset="0" stop-color="#C3D2D8"/>
        <stop offset="0.35" stop-color="#F4F8FA"/>
        <stop offset="0.7" stop-color="#E6EEF1"/>
        <stop offset="1" stop-color="#B9CBD3"/>
      </linearGradient>
      <linearGradient id="backSweep" x1="0" y1="0" x2="1" y2="1">
        <stop offset="0" stop-color="#0077C4"/>
        <stop offset="0.4" stop-color="#6FCCEA"/>
        <stop offset="0.65" stop-color="#00A9DD"/>
        <stop offset="1" stop-color="#0077C4"/>
      </linearGradient>
    </defs>
    <rect width="1000" height="390" fill="url(#backBody)"/>
    <path d="M515 0 C 700 40, 800 150, 785 262 C 780 320, 765 360, 751 390 L1000 390 L1000 0 Z" fill="url(#backSweep)"/>
    <rect x="956" width="44" height="390" fill="#0A7FCB"/>
    <g stroke="#0069B3" stroke-width="2">
      <line x1="956" y1="20" x2="1000" y2="20"/><line x1="956" y1="50" x2="1000" y2="50"/>
      <line x1="956" y1="80" x2="1000" y2="80"/><line x1="956" y1="110" x2="1000" y2="110"/>
      <line x1="956" y1="140" x2="1000" y2="140"/><line x1="956" y1="170" x2="1000" y2="170"/>
      <line x1="956" y1="200" x2="1000" y2="200"/><line x1="956" y1="230" x2="1000" y2="230"/>
      <line x1="956" y1="260" x2="1000" y2="260"/><line x1="956" y1="290" x2="1000" y2="290"/>
      <line x1="956" y1="320" x2="1000" y2="320"/><line x1="956" y1="350" x2="1000" y2="350"/>
    </g>
  </svg>

  <div class="care-column">
    <div class="care-title">PREMIUM ORAL<br>CARE DURING<br>ORTHODONTIC<br>TREATMENT</div>
    <div class="care-art" role="img" aria-label="Illustration of teeth with metal braces and teeth with clear aligners"></div>
    <ul class="care-list">
      <li>Prevent Cavity</li>
      <li>Freshen Breath</li>
      <li>Strengthen Teeth</li>
    </ul>
  </div>

  <div class="usage">
    <p><span class="usage__head">Directions:</span> Apply at least one inch<br>strip of the product onto a soft bristle<br>toothbrush. Brush teeth thoroughly, for at least<br>three minutes twice a day.</p>
    <p><span class="usage__head">Ingredients:</span> Aqua, Sorbitol, Hydrated Silica, Glycerin,<br>PEG-12, Sodium Lauryl Sulfate, Aroma, Cellulose Gum,<br>Titanium Dioxide, Potassium Sorbate, Allantoin, Sodium<br>Fluoride, Citric Acid, Peppermint Essence, Sodium<br>Saccharin, CI 47005, CI 42090, Cinnamal.</p>
  </div>

  <div class="warnings">
    <div class="warnings__head">Warnings:</div>
    Do not ingest.<br>Keep out of reach<br>of children under<br>6 years of age.
  </div>

  <div class="brand brand--back">quorlume<span class="brand__dot"></span></div>
</section>

</body>
</html>
```